The Little Sprouts Forum -Flyer Design

The flyer is for a conference that is being held for Chiropractors to gain continuing education in paediatrics with all proceeds from the event going to paediatric research.

Paediatric chiropractic is mostly about how we can help the body and brain develop optimally with a big focus of the nervous system. I have attached the logo and the website is www.littlesproutsforum.example. The feel should be kid friendly but also professional. It is also going to be largely for the American Market.

Here is an outline of the copy that we need on this flyer:
========================================
Don’t Miss This….some of the best minds in Chiropractic Pediatrics…all together in the USA.

23-24th April 2016, San Francisco. Sat 23rd 8.30-5.30 Sun 24th 8.30am -1pm

Harborview Lodge by Marwell, ​Bayline Terminal-Pierside

With all proceeds going directly to Pediatric based research projects at the Institute for Spinal Wellness Studies at QMPA.

Learn From:

Dr. Marlene Voskuil
Dr. Ingrid Wemkoss
Dr. Fabiola Trennick
Dr. Marianne Pollux
Dr. Terry Vanlund
Dr. Josephine Amsworth
Dr. Lavinia Amsworth
Dr. Greta Pomberg
Dr. Nadia Folck
Dr. Celine Marsh

Early bird $449 18th Mar 2016

CE available

More info at www.littlesproutsforum.example (could we also have a Facebook icon too!)

```html
<!DOCTYPE html>
<html lang="en">
<head>
<meta charset="utf-8">
<title>The Little Sprouts Forum – Flyer</title>
<link href="https://fonts.googleapis.com/css2?family=Arvo:wght@400;700&display=swap" rel="stylesheet">
<style>
  :root {
    --orange: #ea5a1c;
    --orange-deep: #e0401a;
    --charcoal: #2b2b2b;
    --green: #74a02a;
    --ink: #2a2a2a;
    --white: #ffffff;
    --portrait: #c9c4bf;
  }
  * { box-sizing: border-box; margin: 0; padding: 0; }
  html, body { width: 1046px; height: 1200px; overflow: hidden; background: var(--white); }
  body { font-family: "Arvo", Georgia, serif; color: var(--ink); }

  .flyer { position: relative; width: 1046px; height: 1200px; overflow: hidden; background: var(--white); }

  .header-art { position: absolute; left: 0; top: 0; width: 1046px; height: 580px; }

  .brand { position: absolute; left: 56px; top: 46px; display: flex; align-items: center; gap: 12px; }
  .brand-dot { width: 28px; height: 28px; border-radius: 50%; background: var(--orange); }
  .brand-name { font-size: 28px; font-weight: 700; color: var(--green); }

  .headline { position: absolute; left: 76px; top: 170px; color: var(--white); }
  .headline h1 { font-weight: 400; font-size: 38px; line-height: 1.2; }
  .headline .dates { margin-top: 14px; font-size: 27px; line-height: 1.3; }

  .venue { position: absolute; right: 56px; top: 440px; text-align: right; color: var(--white); font-size: 20px; line-height: 1.35; }

  .proceeds { position: absolute; left: 0; right: 0; top: 588px; text-align: center; font-size: 20px; line-height: 1.35; }

  .learn-title { position: absolute; left: 0; right: 0; top: 648px; text-align: center; color: var(--orange); font-size: 34px; font-weight: 400; }

  .speakers { position: absolute; left: 60px; right: 60px; top: 706px; display: grid; grid-template-columns: repeat(5, 1fr); row-gap: 12px; }
  .speaker { display: flex; flex-direction: column; align-items: center; text-align: center; }
  .speaker-ring { width: 118px; height: 118px; border-radius: 50%; border: 5px solid transparent; border-top-color: var(--green); border-left-color: var(--green); padding: 5px; transform: rotate(20deg); }
  .speaker-photo { width: 100%; height: 100%; border-radius: 50%; background: radial-gradient(circle at 50% 40%, #ddd6cf, var(--portrait) 70%); }
  .speaker-name { margin-top: 6px; font-size: 15px; line-height: 1.25; height: 38px; max-width: 170px; }

  .early-bird { position: absolute; left: 290px; top: 1062px; background: var(--green); color: var(--white); font-size: 21px; padding: 8px 24px; border-radius: 8px; }

  .footer-art { position: absolute; left: 0; bottom: 0; width: 1046px; height: 90px; }
  .web-line { position: absolute; right: 56px; bottom: 16px; display: flex; align-items: center; gap: 10px; color: var(--white); font-size: 20px; }
  .web-mark { width: 18px; height: 18px; background: var(--white); }
</style>
</head>
<body>
<main class="flyer">

  <svg class="header-art" viewBox="0 0 1046 580">
    <defs>
      <clipPath id="header-shape">
        <path d="M0,150 C300,120 650,60 1046,0 L1046,500 C700,540 360,570 0,550 Z"/>
      </clipPath>
      <linearGradient id="photo-tone" x1="0" y1="0" x2="1" y2="1">
        <stop offset="0" stop-color="#f07a3e"/>
        <stop offset="1" stop-color="#e8612a"/>
      </linearGradient>
    </defs>
    <path d="M0,150 C300,120 650,60 1046,0 L1046,500 C700,540 360,570 0,550 Z" fill="var(--orange)"/>
    <g clip-path="url(#header-shape)">
      <rect role="img" aria-label="Photo of a conference talk slide showing a crawling baby" x="460" y="40" width="586" height="520" fill="url(#photo-tone)"/>
    </g>
    <path d="M380,548 C600,450 850,390 1046,368 L1046,500 C800,525 600,542 380,548 Z" fill="var(--charcoal)"/>
  </svg>

  <div class="brand">
    <span class="brand-dot"></span>
    <span class="brand-name">The Little Sprouts Forum</span>
  </div>

  <header class="headline">
    <h1>DON'T MISS THIS….<br>Some of the best minds<br>in Chiropractic Pediatrics…<br>All together in the USA.</h1>
    <p class="dates">23-24th April 2016, San Francisco.<br>Sat 23rd 8.30-5.30<br>Sun 24th 8.30am -1pm</p>
  </header>

  <p class="venue">Harborview Lodge by Marwell,<br>Bayline Terminal-Pierside</p>

  <p class="proceeds">With all proceeds going directly to Pediatric based research<br>projects at the Institute for Spinal Wellness Studies at QMPA.</p>

  <h2 class="learn-title">LEARN FROM</h2>

  <section class="speakers">
    <div class="speaker"><div class="speaker-ring"><div class="speaker-photo" role="img" aria-label="Portrait of Dr. Marlene Voskuil"></div></div><p class="speaker-name">Dr. Marlene Voskuil</p></div>
    <div class="speaker"><div class="speaker-ring"><div class="speaker-photo" role="img" aria-label="Portrait of Dr. Ingrid Wemkoss"></div></div><p class="speaker-name">Dr. Ingrid Wemkoss</p></div>
    <div class="speaker"><div class="speaker-ring"><div class="speaker-photo" role="img" aria-label="Portrait of Dr. Fabiola Trennick"></div></div><p class="speaker-name">Dr. Fabiola<br>Trennick</p></div>
    <div class="speaker"><div class="speaker-ring"><div class="speaker-photo" role="img" aria-label="Portrait of Dr. Marianne Pollux"></div></div><p class="speaker-name">Dr. Marianne Pollux</p></div>
    <div class="speaker"><div class="speaker-ring"><div class="speaker-photo" role="img" aria-label="Portrait of Dr. Terry Vanlund"></div></div><p class="speaker-name">Dr. Terry Vanlund</p></div>
    <div class="speaker"><div class="speaker-ring"><div class="speaker-photo" role="img" aria-label="Portrait of Dr. Josephine Amsworth"></div></div><p class="speaker-name">Dr. Josephine<br>Amsworth</p></div>
    <div class="speaker"><div class="speaker-ring"><div class="speaker-photo" role="img" aria-label="Portrait of Dr. Lavinia Amsworth"></div></div><p class="speaker-name">Dr. Lavinia<br>Amsworth</p></div>
    <div class="speaker"><div class="speaker-ring"><div class="speaker-photo" role="img" aria-label="Portrait of Dr. Greta Pomberg"></div></div><p class="speaker-name">Dr. Greta Pomberg</p></div>
    <div class="speaker"><div class="speaker-ring"><div class="speaker-photo" role="img" aria-label="Portrait of Dr. Nadia Folck"></div></div><p class="speaker-name">Dr. Nadia Folck</p></div>
    <div class="speaker"><div class="speaker-ring"><div class="speaker-photo" role="img" aria-label="Portrait of Dr. Celine Marsh"></div></div><p class="speaker-name">Dr. Celine Marsh</p></div>
  </section>

  <p class="early-bird">EARLY BIRD $449 18TH MAR 2016</p>

  <svg class="footer-art" viewBox="0 0 1046 90" aria-hidden="true">
    <path d="M0,40 C200,10 420,0 620,30 C420,30 200,50 0,90 Z" fill="var(--orange-deep)"/>
    <path d="M300,90 C520,50 780,30 1046,20 L1046,90 Z" fill="var(--green)"/>
  </svg>
  <p class="web-line"><span>www.littlesproutsforum.example</span><span class="web-mark" aria-hidden="true"></span></p>

</main>
</body>
</html>
```